Card for Real Estate Developer

We need a business card design for a Real Estate Development company based in Texas. We focus on retail, apartment and residential development. Our target is predominantly investors looking to us to place their money properly to achieve a significant return. On the other side we sell our services to large retailers as their preferred developer assisting them in locating, building and leasing their real estate.

Target Market(s)

Investors

Industry/Entity Type

Real Estate Development

Contact Information for Business Card

Would like to stay within the company color scheme, while keeping the design moderately simple.

Font styles to use
Other font styles liked:
• per attached document

Requirements
Must have
• Name
• Phone
• Email
• Website
• Logo Prominently Displayed
• Stay within the colors provided in the attached document

```html
<!DOCTYPE html>
<html lang="en">
<head>
<meta charset="utf-8">
<title>Halvern Development – Business Card</title>
<link href="https://fonts.googleapis.com/css2?family=Cinzel:wght@400;600&family=Open+Sans:wght@400;600&display=swap" rel="stylesheet">
<style>
  :root {
    --backdrop: #2e2e2e;
    --card: #000000;
    --accent: #6fb8dc;
    --ink: #ffffff;
    --muted: #d9d9d9;
  }
  * { box-sizing: border-box; margin: 0; padding: 0; }
  html, body { width: 1200px; height: 900px; overflow: hidden; }
  body {
    background: var(--backdrop);
    font-family: "Open Sans", Arial, sans-serif;
    color: var(--ink);
    position: relative;
  }
  .card {
    position: absolute;
    left: 267px;
    width: 665px;
    height: 380px;
    background: var(--card);
    box-shadow: 0 10px 30px rgba(0,0,0,0.55);
  }
  .card--front { top: 40px; }
  .card--back { top: 480px; }

  /* Front */
  .front-brand {
    position: absolute;
    left: 0; right: 0; top: 140px;
    display: flex; align-items: center; justify-content: center; gap: 16px;
  }
  .brand-square { width: 26px; height: 26px; background: var(--accent); }
  .brand-name {
    font-family: "Cinzel", Georgia, serif;
    font-weight: 400;
    font-size: 36px;
    letter-spacing: 3px;
    color: var(--accent);
    white-space: nowrap;
  }
  .front-web {
    position: absolute;
    left: 0; right: 0; top: 212px;
    text-align: center;
    font-size: 17px;
    letter-spacing: 1px;
    color: var(--ink);
  }

  /* Back */
  .back-brand {
    position: absolute;
    left: 45px; top: 85px;
    display: flex; align-items: center; gap: 12px;
  }
  .back-brand .brand-square { width: 18px; height: 18px; }
  .back-brand .brand-name { font-size: 25px; letter-spacing: 2px; color: var(--ink); }

  .person {
    position: absolute;
    right: 55px; top: 196px;
    text-align: right;
  }
  .person-name {
    font-family: "Cinzel", Georgia, serif;
    font-size: 24px;
    letter-spacing: 1.5px;
    color: var(--accent);
    line-height: 1;
    white-space: nowrap;
  }
  .person-bar {
    position: absolute;
    right: 30px; top: 186px;
    width: 12px; height: 44px;
    background: var(--accent);
    border-left: 3px solid var(--ink);
  }
  .rule-accent {
    position: absolute;
    left: 40px; top: 240px;
    width: 400px; height: 1.5px;
    background: var(--accent);
  }
  .rule-light {
    position: absolute;
    left: 440px; top: 240px;
    width: 170px; height: 1.5px;
    background: var(--ink);
  }
  .person-title {
    position: absolute;
    right: 55px; top: 245px;
    font-size: 10px;
    letter-spacing: 1px;
    color: var(--ink);
  }
  .contacts {
    position: absolute;
    left: 45px; top: 262px;
    list-style: none;
  }
  .contacts li {
    display: flex; align-items: center; gap: 10px;
    font-size: 15px;
    line-height: 24px;
    color: var(--muted);
    white-space: nowrap;
  }
  .contacts svg { width: 12px; height: 12px; flex: none; }
</style>
</head>
<body>

<section class="card card--front" aria-label="Card front">
  <div class="front-brand">
    <span class="brand-square"></span>
    <span class="brand-name">HALVERN DEVELOPMENT</span>
  </div>
  <p class="front-web">www.halverndevelopment.com</p>
</section>

<section class="card card--back" aria-label="Card back">
  <div class="back-brand">
    <span class="brand-square"></span>
    <span class="brand-name">HALVERN DEVELOPMENT</span>
  </div>

  <div class="person-bar"></div>
  <div class="person">
    <p class="person-name">MARCUS REED</p>
  </div>
  <div class="rule-accent"></div>
  <div class="rule-light"></div>
  <p class="person-title">DIRECTOR</p>

  <ul class="contacts">
    <li>
      <svg viewBox="0 0 24 24" aria-hidden="true"><path fill="var(--accent)" d="M6.6 10.8a15 15 0 0 0 6.6 6.6l2.2-2.2c.3-.3.7-.4 1-.2 1.1.4 2.3.6 3.6.6.6 0 1 .4 1 1V20c0 .6-.4 1-1 1C10.6 21 3 13.4 3 4c0-.6.4-1 1-1h3.5c.6 0 1 .4 1 1 0 1.3.2 2.5.6 3.6.1.3 0 .7-.2 1z"/></svg>
      <span>+512 7384-1206</span>
    </li>
    <li>
      <svg viewBox="0 0 24 24" aria-hidden="true"><rect x="2" y="5" width="20" height="14" fill="none" stroke="var(--accent)" stroke-width="2"/><path d="M2 6l10 7 10-7" fill="none" stroke="var(--accent)" stroke-width="2"/></svg>
      <span>info@halverndevelopment.com</span>
    </li>
    <li>
      <svg viewBox="0 0 24 24" aria-hidden="true"><circle cx="12" cy="12" r="10" fill="none" stroke="var(--accent)" stroke-width="2"/><path d="M2 12h20M12 2c3 3 3 17 0 20M12 2c-3 3-3 17 0 20" fill="none" stroke="var(--accent)" stroke-width="1.6"/></svg>
      <span>www.halverndevelopment.com</span>
    </li>
  </ul>
</section>

</body>
</html>
```